Design for Chirpwall Ad to promote Laptops purchase

Need a graphic design for a Chirpwall Ad - to promote 2 laptops (PC and Zorvane) with the stated required ad-text.

AD TEXT:

FOR SME BUSINESS ONLY!
Chat with us!
To get advice on how to apply
and defray up to 80%* of business laptop purchase cost!

*Terms and Conditions apply

Image for reference only

Target Market(s)

Small medium business

Font styles to use
Sans Serif

Requirements
Must have
• 2 laptop images (see attached ) - 1 vector image of ZORVANE , and pls try to create another vector image of PC laptop (where screen is showing Blue Pendrel screen)

```html
<!DOCTYPE html>
<html lang="en">
<head>
<meta charset="utf-8">
<title>Business Laptop Grant Ad</title>
<link rel="stylesheet" href="https://fonts.googleapis.com/css2?family=Arimo:wght@400&family=Roboto:wght@400;500;700;900&display=swap">
<style>
  :root {
    --bg-light: #f4f9fd;
    --bg-mist: #d9ecf8;
    --sky: #5ec3f2;
    --ocean: #1f8fd6;
    --navy: #3a5382;
    --panel-top: #4a9ad8;
    --panel-bottom: #2c5f9e;
    --white: #ffffff;
    --notice-red: #e01818;
    --tag-fill: #3a5382;
    --pc-blue: #2f7fd8;
    --pc-silver: #c9cdd3;
    --zv-violet: #6b4a86;
    --zv-silver: #d6d9de;
  }
  * { box-sizing: border-box; margin: 0; padding: 0; }
  html, body { width: 1200px; height: 444px; overflow: hidden; background: var(--white); }
  .ad {
    position: relative;
    width: 1200px;
    height: 444px;
    overflow: hidden;
    font-family: "Roboto", Arial, sans-serif;
    background: radial-gradient(ellipse at 30% 55%, var(--bg-light) 0%, var(--bg-mist) 70%, #cfe6f6 100%);
  }
  .bands { position: absolute; inset: 0; }
  .notice {
    position: absolute;
    left: 40px;
    top: 26px;
    font-family: "Arimo", Arial, sans-serif;
    color: var(--notice-red);
    font-size: 19px;
    line-height: 23px;
  }
  .notice p:first-child { padding-left: 4px; }

  .product {
    position: absolute;
    border-radius: 10px;
  }
  .product--pc {
    left: 44px; top: 172px; width: 278px; height: 164px;
    background: linear-gradient(180deg, var(--pc-blue) 0%, #3b8be0 70%, var(--pc-silver) 100%);
  }
  .product--zorvane {
    left: 340px; top: 38px; width: 264px; height: 250px;
    background: linear-gradient(180deg, var(--zv-violet) 0%, #a872b8 45%, #c4b8cc 75%, var(--zv-silver) 100%);
  }

  .offer {
    position: absolute;
    left: 762px; top: 34px;
    width: 418px; height: 326px;
  }
  .offer svg { position: absolute; inset: 0; }
  .offer__body {
    position: absolute; inset: 0;
    color: var(--white);
    text-align: center;
  }
  .offer__chat { position: absolute; top: 62px; left: 0; right: 0; font-size: 21px; font-weight: 400; letter-spacing: 0.3px; }
  .offer__chat strong { font-weight: 900; }
  .offer__sub { position: absolute; top: 88px; left: 0; right: 0; font-size: 13px; font-weight: 500; letter-spacing: 0.3px; }
  .offer__rule { position: absolute; left: 44px; right: 44px; height: 3px; background: var(--white); }
  .offer__rule--top { top: 123px; }
  .offer__rule--bottom { top: 210px; }
  .offer__headline {
    position: absolute; top: 136px; left: 0; right: 0;
    font-size: 31px; font-weight: 700; line-height: 35px; letter-spacing: 0.3px;
  }
  .offer__terms {
    position: absolute; top: 265px; left: 0; right: 0;
    font-size: 14px; font-weight: 500; line-height: 19px; letter-spacing: 0.3px;
  }

  .contact {
    position: absolute;
    height: 31px;
    color: var(--white);
    font-weight: 700;
    font-size: 16px;
    letter-spacing: 0.2px;
  }
  .contact svg.contact__shape { position: absolute; inset: 0; }
  .contact__label {
    position: absolute; top: 6px; right: 44px;
    line-height: 20px;
    white-space: nowrap;
  }
  .contact__icon { position: absolute; top: 6px; right: 12px; width: 20px; height: 20px; }
  .contact--email { left: 582px; top: 244px; width: 177px; }
  .contact--phone { left: 578px; top: 283px; width: 181px; }
  .contact--location { left: 553px; top: 321px; width: 206px; }
</style>
</head>
<body>
<div class="ad">
  <svg class="bands" width="1200" height="444" viewBox="0 0 1200 444" aria-hidden="true">
    <polygon points="811,0 1200,0 1200,444 578,444" fill="var(--sky)"/>
    <polygon points="940,0 1200,0 1200,444 660,444" fill="var(--ocean)"/>
    <polygon points="1045,0 1200,0 1200,444 833,444" fill="var(--navy)"/>
  </svg>

  <div class="notice">
    <p>Image for reference only</p>
    <p>*Terms and Conditions apply</p>
  </div>

  <div class="product product--pc" role="img" aria-label="PC laptop, open, its screen showing a blue Pendrel error screen"></div>
  <div class="product product--zorvane" role="img" aria-label="Silver Zorvane laptop, open, with a violet and pink screen, seen from the side"></div>

  <div class="contact contact--email">
    <svg class="contact__shape" viewBox="0 0 177 31" preserveAspectRatio="none" aria-hidden="true">
      <polygon points="10,1.5 176,1.5 176,29.5 1.5,29.5" fill="var(--tag-fill)" stroke="var(--white)" stroke-width="2"/>
    </svg>
    <span class="contact__label">YOUREMAIL</span>
    <svg class="contact__icon" viewBox="0 0 20 20" aria-hidden="true">
      <rect x="2" y="4" width="16" height="12" fill="none" stroke="var(--white)" stroke-width="1.6"/>
      <polyline points="2,4 10,11 18,4" fill="none" stroke="var(--white)" stroke-width="1.6"/>
    </svg>
  </div>

  <div class="contact contact--phone">
    <svg class="contact__shape" viewBox="0 0 181 31" preserveAspectRatio="none" aria-hidden="true">
      <polygon points="10,1.5 180,1.5 180,29.5 1.5,29.5" fill="var(--tag-fill)" stroke="var(--white)" stroke-width="2"/>
    </svg>
    <span class="contact__label">YOURPHONE</span>
    <svg class="contact__icon" viewBox="0 0 20 20" aria-hidden="true">
      <path d="M5 2 L8 2 L9 6 L7 8 C8 11 9.5 12.5 12 13.5 L14 11.5 L18 12.5 L18 15.5 C18 17 16.5 18 15 17.5 C8.5 16 4 11.5 2.5 5 C2 3.5 3.3 2 5 2 Z" fill="var(--white)"/>
    </svg>
  </div>

  <div class="contact contact--location">
    <svg class="contact__shape" viewBox="0 0 206 31" preserveAspectRatio="none" aria-hidden="true">
      <polygon points="10,1.5 205,1.5 205,29.5 1.5,29.5" fill="var(--tag-fill)" stroke="var(--white)" stroke-width="2"/>
    </svg>
    <span class="contact__label">YOURLOCATION</span>
    <svg class="contact__icon" viewBox="0 0 20 20" aria-hidden="true">
      <path d="M10 1 C6.3 1 4 3.8 4 7 C4 11.5 10 19 10 19 C10 19 16 11.5 16 7 C16 3.8 13.7 1 10 1 Z" fill="var(--white)"/>
      <circle cx="10" cy="7" r="2.4" fill="var(--tag-fill)"/>
    </svg>
  </div>

  <div class="offer">
    <svg viewBox="0 0 418 326" width="418" height="326" aria-hidden="true">
      <defs>
        <linearGradient id="offerFill" x1="0" y1="0" x2="0.4" y2="1">
          <stop offset="0" stop-color="var(--panel-top)"/>
          <stop offset="1" stop-color="var(--panel-bottom)"/>
        </linearGradient>
      </defs>
      <polygon points="49,2.5 416,2.5 416,323.5 2.5,323.5 2.5,106" fill="url(#offerFill)" stroke="var(--white)" stroke-width="4"/>
    </svg>
    <div class="offer__body">
      <p class="offer__chat">CHAT <strong>WITH US!</strong></p>
      <p class="offer__sub">TO GET ADVICE ON HOW TO APPLY</p>
      <div class="offer__rule offer__rule--top"></div>
      <h1 class="offer__headline">FOR SME<br>BUSINESS ONLY!</h1>
      <div class="offer__rule offer__rule--bottom"></div>
      <p class="offer__terms">AND DEFRAY UP TO 80%* OF BUSINESS<br>LAPTOP PURCHASE COST!</p>
    </div>
  </div>
</div>
</body>
</html>
```